Dunwick Realty & Management, LLC
Sunny Florida Real Estate -- Business Card - Real Estate
Sunny Florida Real Estate -- Business Card
Professional
Marcus Tolver, CRS
Broker / Sales Associate
4875 Briar Creek Lane Tallahassee, FL 32398-1147
marcustolver@dunwickrealty.example
www.dunwickrealty.example
BK5804419
Incorporate head shot into front of card.
marcustolver marcustolver
Mailing address has been changed: The new address for the business card is: 2609 Hollow Ash Court Tallahassee, FL 32398-2256
Zip code is 32398-2274

```html
<!DOCTYPE html>
<html lang="en">
<head>
<meta charset="utf-8">
<title>Dunwick Realty &amp; Management — Stationery Set</title>
<link href="https://fonts.googleapis.com/css2?family=Open+Sans:wght@400;600;700&display=swap" rel="stylesheet">
<style>
:root{
  --bg:#e9eaeb;
  --paper:#ffffff;
  --charcoal:#3a3d41;
  --charcoal-deep:#2b2d30;
  --lime:#a9c63d;
  --gold:#e2b22b;
  --blue:#2d6bb3;
  --ink:#4a4d52;
  --muted:#8c9096;
  --soft:#c7c9cc;
  --photo-a:#7b6a5c;
  --photo-b:#c9c1b8;
}
*{box-sizing:border-box;margin:0;padding:0}
html,body{width:1200px;height:373px;overflow:hidden}
body{background:linear-gradient(#f3f3f4,var(--bg));font-family:"Open Sans",Arial,sans-serif;color:var(--ink);position:relative}
.piece{position:absolute;background:var(--paper);box-shadow:0 2px 6px rgba(0,0,0,.18)}
.label{position:absolute;font-size:6px;color:var(--muted);text-align:center;width:100%;bottom:-11px;left:0;white-space:nowrap}
.brand{font-weight:700;color:var(--charcoal);letter-spacing:.3px;line-height:1.15;white-space:nowrap}
.brand small{display:block;font-weight:600;color:var(--lime);font-size:.6em;letter-spacing:.2px}
.dot{display:inline-block;border-radius:50%;background:var(--lime);vertical-align:middle}
.tiny{font-size:4px;line-height:1.45;color:var(--muted);white-space:nowrap}

/* letterhead */
.letterhead{left:19px;top:67px;width:118px;height:168px}
.letterhead .brand{position:absolute;left:8px;top:10px;font-size:6px}
.letterhead .contact{position:absolute;right:8px;top:10px;text-align:right}
.letterhead .foot{position:absolute;left:0;right:0;bottom:10px;height:4px;background:var(--charcoal)}
.letterhead .foot::after{content:"";position:absolute;left:0;top:-3px;width:55%;height:3px;background:var(--lime)}

/* envelope */
.envelope{left:19px;top:270px;width:211px;height:90px}
.envelope .brand{position:absolute;left:10px;top:10px;font-size:6px}
.envelope .band{position:absolute;left:0;right:0;bottom:0;height:22px;background:var(--charcoal)}
.envelope .band::before{content:"";position:absolute;left:0;top:-4px;width:60%;height:4px;background:var(--lime)}

/* card fronts */
.card{width:140px;height:89px}
.card-front-a{left:252px;top:79px}
.card-front-b{left:420px;top:79px}
.card .photo{position:absolute;left:6px;top:12px;width:46px;height:56px;background:linear-gradient(160deg,var(--photo-b),var(--photo-a))}
.card .brand{position:absolute;left:60px;top:12px;font-size:5.5px}
.card .who{position:absolute;left:60px;top:36px;font-size:5px;font-weight:700;color:var(--charcoal);line-height:1.35;white-space:nowrap}
.card .who span{display:block;font-weight:400;font-size:4px;color:var(--muted)}
.card .strip{position:absolute;left:0;right:0;bottom:0;height:10px;background:var(--charcoal)}
.card .strip::before{content:"";position:absolute;left:0;top:-2px;width:50%;height:2px;background:var(--lime)}

/* card backs */
.card-back{left:420px;width:146px;height:79px;background:var(--charcoal-deep)}
.card-back-a{top:180px}
.card-back-b{top:276px}
.card-back .badge{position:absolute;left:10px;top:12px;width:22px;height:22px;border-radius:50%;background:var(--gold)}
.card-back .tag{position:absolute;left:38px;top:14px;font-size:5.5px;font-weight:700;color:var(--gold);line-height:1.35;white-space:nowrap}
.card-back .tag span{display:block;font-weight:400;font-size:4px;color:var(--soft)}
.card-back .bar{position:absolute;left:0;right:0;bottom:14px;height:12px;background:var(--blue)}
.card-back .bar p{font-size:4.5px;color:#fff;padding:3px 10px;white-space:nowrap}

/* folders */
.folder-cover{left:636px;top:12px;width:252px;height:348px;background:linear-gradient(90deg,#f5f6f7,#e4e6e8)}
.folder-cover .brand{position:absolute;left:0;right:0;top:140px;text-align:center;font-size:12px}
.folder-cover .brand .dot{width:14px;height:14px;margin-right:6px}
.folder-cover .bottom{position:absolute;left:0;right:0;bottom:0;height:46px;background:var(--charcoal)}
.folder-cover .bottom::before{content:"";position:absolute;left:0;top:-6px;width:70%;height:6px;background:var(--lime)}
.folder-open{left:900px;top:12px;width:288px;height:348px;background:linear-gradient(90deg,#e2e4e6,#f7f8f9 50%,#eceef0)}
.folder-open .pocket{position:absolute;left:150px;right:0;bottom:0;height:130px;background:var(--charcoal)}
.folder-open .pocket::before{content:"";position:absolute;left:0;right:0;top:-5px;height:5px;background:var(--lime)}
.folder-open .pocket-left{position:absolute;left:0;width:140px;bottom:0;height:110px;background:#d3d6d9}
.folder-open .slot-card{position:absolute;left:190px;top:235px;width:70px;height:42px;background:var(--paper)}
.folder-open .slot-card .photo{position:absolute;left:4px;top:6px;width:20px;height:26px;background:linear-gradient(160deg,var(--photo-b),var(--photo-a))}
.folder-open .slot-card .brand{position:absolute;left:28px;top:8px;font-size:4px}
</style>
</head>
<body>

<section class="piece letterhead">
  <div class="brand">Dunwick Realty<small>&amp; Management, LLC</small></div>
  <div class="contact tiny">4875 Briar Creek Lane<br>Tallahassee, FL 32398-1147<br>www.dunwickrealty.example</div>
  <div class="foot"></div>
  <p class="label">Letterhead</p>
</section>

<section class="piece envelope">
  <div class="brand">Dunwick Realty<small>&amp; Management, LLC</small></div>
  <div class="band"></div>
  <p class="label">Envelope</p>
</section>

<section class="piece card card-front-a">
  <div class="photo" role="img" aria-label="Head shot of Marcus Tolver"></div>
  <div class="brand">Dunwick Realty<small>&amp; Management, LLC</small></div>
  <div class="who">Marcus Tolver, CRS<span>Broker / Sales Associate</span><span>BK5804419</span></div>
  <div class="strip"></div>
  <p class="label">Card Front</p>
</section>

<section class="piece card card-front-b">
  <div class="photo" role="img" aria-label="Head shot of Marcus Tolver"></div>
  <div class="brand">Dunwick Realty<small>&amp; Management, LLC</small></div>
  <div class="who">Marcus Tolver, CRS<span>Broker / Sales Associate</span><span>www.dunwickrealty.example</span></div>
  <div class="strip"></div>
</section>

<section class="piece card-back card-back-a">
  <div class="badge"></div>
  <div class="tag">Dunwick Realty<span>2609 Hollow Ash Court</span><span>Tallahassee, FL 32398-2256</span></div>
  <div class="bar"><p>(850) 555-0142 · www.dunwickrealty.example</p></div>
  <p class="label">Card Back</p>
</section>

<section class="piece card-back card-back-b">
  <div class="badge"></div>
  <div class="tag">Dunwick Realty<span>Tallahassee, FL 32398-2274</span></div>
  <div class="bar"><p>(850) 555-0142 · marcustolver</p></div>
</section>

<section class="piece folder-cover">
  <div class="brand"><span class="dot"></span>DUNWICK REALTY<small>&amp; Management, LLC</small></div>
  <div class="bottom"></div>
  <p class="label">Folder Cover</p>
</section>

<section class="piece folder-open">
  <div class="pocket-left"></div>
  <div class="pocket"></div>
  <div class="slot-card">
    <div class="photo" role="img" aria-label="Head shot of Marcus Tolver"></div>
    <div class="brand">Dunwick Realty<small>&amp; Management</small></div>
  </div>
  <p class="label">Folder Inside</p>
</section>

</body>
</html>
```